A4 Flyer

Brightwell Care Academy is starting a course in regional Victoria. We are currently advertising (See attached file A34984) in local papers but need to create a one page flyer to distribute to Aged Care facilities in the area. The A4 flyer will be inserted into a folder pack with more detailed information on Brightwell Care Academy. Important to use images and logoes attached

Target Market(s)

Flyer to be distributed to Aged Care facility staff and owners

Industry/Entity Type

Advertising

Font styles to use
Sans Serif

Colors
f37123
ec1f27

Requirements
Must have
• BCA Logo
Some image

```html
<!DOCTYPE html>
<html lang="en">
<head>
<meta charset="utf-8">
<title>Brightwell Care Academy – Course Flyer</title>
<link href="https://fonts.googleapis.com/css2?family=Oswald:wght@500;600&family=Open+Sans:wght@400;600;700&display=swap" rel="stylesheet">
<style>
  :root {
    --orange: #f37123;
    --red: #ec1f27;
    --charcoal: #4a4a4a;
    --charcoal-dark: #3d3d3d;
    --ink: #444444;
    --muted: #6a6a6a;
    --paper: #ffffff;
    --stage: #ececec;
  }
  * { box-sizing: border-box; margin: 0; padding: 0; }
  html, body { width: 1200px; height: 740px; overflow: hidden; }
  body {
    background: var(--stage);
    font-family: "Open Sans", Arial, sans-serif;
    position: relative;
  }
  .flyer {
    position: absolute;
    left: 340px; top: 9px;
    width: 520px; height: 722px;
    background: linear-gradient(180deg, #ffffff 0%, #f4f4f4 100%);
    box-shadow: 0 4px 18px rgba(0,0,0,.18);
    overflow: hidden;
  }
  .top-strip { position: absolute; left: 0; top: 0; width: 520px; height: 14px; }

  .brand { position: absolute; left: 30px; top: 42px; display: flex; align-items: center; gap: 12px; }
  .brand-dot { width: 40px; height: 40px; border-radius: 50%; background: var(--orange); flex: none; }
  .brand-name { color: var(--orange); font-weight: 600; font-size: 21px; line-height: 1.1; }

  .session-info {
    position: absolute; left: 330px; top: 44px; width: 160px;
    text-align: center; color: var(--muted); font-size: 13.5px; line-height: 1.35;
  }

  .photo {
    position: absolute; border: 6px solid #fff;
    box-shadow: 0 3px 10px rgba(0,0,0,.25);
  }
  .photo--anatomy { left: 318px; top: 118px; width: 172px; height: 228px; transform: rotate(3deg);
    background: linear-gradient(135deg, #e9e6e2 0%, #cfc9c4 55%, #b9a39a 100%); }
  .photo--student-a { left: 234px; top: 402px; width: 136px; height: 192px; transform: rotate(-1.5deg);
    background: linear-gradient(160deg, #f1f1f1 0%, #dcdcdc 60%, #bfc4cc 100%); }
  .photo--student-b { left: 366px; top: 440px; width: 132px; height: 172px; transform: rotate(2deg);
    background: linear-gradient(160deg, #f2f2f2 0%, #dedede 55%, #9b8f92 100%); }

  .headline-lead {
    position: absolute; left: 26px; top: 132px;
    font-family: "Oswald", "Arial Narrow", sans-serif; font-weight: 500;
    font-size: 46px; color: #555; letter-spacing: .5px;
  }
  .headline-band {
    position: absolute; left: 0; top: 192px; width: 312px; height: 52px;
    background: linear-gradient(90deg, #e8641c, var(--orange));
    color: #fff; font-family: "Oswald", "Arial Narrow", sans-serif; font-weight: 500;
    font-size: 44px; line-height: 52px; padding-left: 26px; letter-spacing: .5px;
  }
  .course-band {
    position: absolute; left: 0; top: 244px; width: 340px; height: 82px;
    background: var(--charcoal); color: #fff; padding: 8px 0 0 26px;
  }
  .course-band h2 {
    font-family: "Oswald", "Arial Narrow", sans-serif; font-weight: 600; font-size: 20px; letter-spacing: .3px;
  }
  .course-band p { font-weight: 600; font-size: 13.5px; line-height: 1.35; }

  .start-badge {
    position: absolute; left: 256px; top: 238px; width: 88px; height: 88px; border-radius: 50%;
    background: radial-gradient(circle at 40% 35%, #f0474c, #c4141b);
    border: 4px solid #fff; box-shadow: 0 2px 8px rgba(0,0,0,.35);
    display: flex; align-items: center; justify-content: center;
  }
  .start-badge span {
    transform: rotate(-14deg); color: #fff; text-align: center;
    font-family: "Oswald", "Arial Narrow", sans-serif; font-weight: 500; font-size: 13px; line-height: 1.1;
  }
  .start-badge strong { display: block; font-size: 18px; font-weight: 600; }

  .funding { position: absolute; left: 26px; top: 355px; color: var(--ink); font-weight: 700; font-size: 14.5px; line-height: 1.45; }
  .modules { position: absolute; left: 30px; top: 410px; list-style: none; color: var(--ink); font-size: 13.5px; line-height: 19px; }
  .modules li::before { content: "•"; margin-right: 8px; }

  .funding-note { position: absolute; left: 26px; top: 610px; color: var(--red); font-weight: 700; font-size: 14.5px; line-height: 1.45; }

  .contact-bar { position: absolute; left: 0; top: 668px; width: 520px; height: 54px; }
  .contact-bar svg { position: absolute; inset: 0; }
  .contact-bar .enrol { position: absolute; left: 30px; top: 17px; color: #fff; font-weight: 600; font-size: 15px; }
  .contact-bar .item { position: absolute; top: 8px; color: #fff; font-weight: 600; font-size: 14.5px; line-height: 1.3; }
  .contact-bar .item--phone { left: 186px; }
  .contact-bar .item--web { left: 360px; }
  .contact-bar .item--web .label { padding-left: 60px; }
</style>
</head>
<body>
  <article class="flyer">
    <svg class="top-strip" viewBox="0 0 520 14" aria-hidden="true">
      <rect x="0" y="0" width="420" height="14" fill="#4a4a4a"/>
      <polygon points="410,0 520,0 520,14 400,14" fill="#f37123"/>
    </svg>

    <div class="brand">
      <span class="brand-dot"></span>
      <span class="brand-name">Brightwell Care<br>Academy</span>
    </div>

    <p class="session-info">Kingsley Nursing<br>Home - Hillview<br>9:00am - 3:00pm</p>

    <div class="photo photo--anatomy" role="img" aria-label="Photo of a trainer with an anatomy model"></div>

    <h1 class="headline-lead">UNIQUE</h1>
    <div class="headline-band">OPPERTUNITY</div>
    <div class="course-band">
      <h2>DOUBLE QUALIFICATION</h2>
      <p>CERT III IN &nbsp;AGED CARE WITH<br>HOME AND COMMUNITY CARE</p>
    </div>

    <div class="start-badge"><span>Fast track<br>Course Start<strong>July 2014</strong></span></div>

    <p class="funding">Goverment Funded for eligible students!<br>Fees from $117</p>

    <ul class="modules">
      <li>Pathology</li>
      <li>Aged Care</li>
      <li>First Aid</li>
      <li>CPR</li>
      <li>Anaphylaxis</li>
      <li>Home &amp; Community Care</li>
      <li>Medications Forr PCA's</li>
      <li>Health Services</li>
    </ul>

    <div class="photo photo--student-a" role="img" aria-label="Photo of a male student at a desk"></div>
    <div class="photo photo--student-b" role="img" aria-label="Photo of a female student at a desk"></div>

    <p class="funding-note">This training is delivered with VIC and<br>Comm Govt. Funding to eligible Students</p>

    <div class="contact-bar">
      <svg viewBox="0 0 520 54" aria-hidden="true">
        <rect x="0" y="0" width="520" height="54" fill="#4a4a4a"/>
        <polygon points="0,0 150,0 136,54 0,54" fill="#f37123"/>
        <line x1="350" y1="10" x2="350" y2="44" stroke="#bdbdbd" stroke-width="1"/>
      </svg>
      <span class="enrol">To Enrol :-</span>
      <p class="item item--phone">Call<br>9555 0142</p>
      <p class="item item--web"><span class="label">Visit</span><br>brightwellcare.com.au</p>
    </div>
  </article>
</body>
</html>
```